First Aid Training business needs business card design

We would like a double sided business card designed for a first aid training business - Brindlewood First Aid. We provide first aid training and , WHS (work, health and safety) training.

The attached word document contains the key information we would like on each side of the business card.

Final design needs to be delivered in print ready format, along with the original file.

```html
<!DOCTYPE html>
<html lang="en">
<head>
<meta charset="utf-8">
<title>Brindlewood First Aid – Business Card</title>
<link href="https://fonts.googleapis.com/css2?family=Roboto+Slab:wght@300;400;600;700&display=swap" rel="stylesheet">
<style>
  :root {
    --red: #e3222a;
    --red-dark: #960b0e;
    --grey-band: #bdbdc2;
    --ink: #111111;
    --text: #3a3a3a;
    --text-light: #5a5a5a;
    --paper: #ffffff;
    --backdrop: #e8e8e4;
  }
  * { margin: 0; padding: 0; box-sizing: border-box; }
  html, body { width: 1200px; height: 810px; overflow: hidden; }
  body { background: var(--backdrop); font-family: "Roboto Slab", serif; position: relative; }

  .card {
    position: absolute;
    left: 310px;
    width: 580px;
    height: 332px;
    background: var(--paper);
    border-radius: 3px;
    overflow: hidden;
  }
  .card--front { top: 50px; }
  .card--back { top: 430px; }

  .band { position: absolute; left: 0; right: 0; }
  .band--top {
    top: 0; height: 42px;
    background: linear-gradient(90deg, var(--paper) 0%, var(--grey-band) 25%, var(--grey-band) 50%, var(--red) 65%, var(--red-dark) 100%);
  }
  .band--bottom {
    bottom: 0; height: 56px;
    background: linear-gradient(90deg, var(--red-dark) 0%, var(--red) 40%, var(--grey-band) 60%, var(--grey-band) 80%, var(--paper) 100%);
  }

  /* Front */
  .brand {
    position: absolute;
    top: 66px; left: 0; right: 0;
    display: flex; align-items: center; justify-content: center; gap: 18px;
  }
  .brand__dot { width: 70px; height: 70px; border-radius: 50%; background: var(--red); flex: none; }
  .brand__name {
    font-weight: 700;
    color: var(--ink);
    font-size: 30px;
    line-height: 1.08;
    letter-spacing: 0.5px;
  }
  .tagline {
    position: absolute; top: 171px; left: 0; right: 0;
    text-align: center; color: var(--red);
    font-weight: 600; font-size: 16px;
  }
  .benefits {
    position: absolute; top: 205px; left: 0; right: 0;
    text-align: center; color: var(--text-light);
    font-weight: 300; font-size: 16.5px; white-space: nowrap;
  }
  .benefits .sep { margin: 0 10px; }
  .services {
    position: absolute; top: 237px; left: 0; right: 0;
    text-align: center; color: var(--text);
    font-weight: 600; font-size: 16.5px;
  }

  /* Back */
  .contact { position: absolute; left: 47px; top: 74px; }
  .contact__name { color: var(--red); font-weight: 600; font-size: 24px; margin-bottom: 16px; }
  .contact__list { list-style: none; }
  .contact__item {
    display: flex; align-items: center; gap: 12px;
    color: var(--text); font-size: 17px; height: 35px;
  }
  .contact__icon { width: 15px; height: 15px; fill: var(--text); flex: none; margin-left: 12px; }
  .divider {
    position: absolute; left: 324px; top: 99px;
    width: 1.5px; height: 138px; background: var(--red);
  }
  .back-brand {
    position: absolute; left: 340px; width: 220px; top: 100px;
    display: flex; flex-direction: column; align-items: center; gap: 12px;
  }
  .back-brand__dot { width: 64px; height: 64px; border-radius: 50%; background: var(--red); }
  .back-brand__name {
    font-weight: 700; color: var(--ink); font-size: 20px;
    line-height: 1.1; text-align: center; letter-spacing: 0.4px;
  }
</style>
</head>
<body>
  <section class="card card--front">
    <div class="band band--top" role="img" aria-label="Decorative red and grey band"></div>

    <div class="brand">
      <span class="brand__dot"></span>
      <div class="brand__name">BRINDLEWOOD<br>FIRST AID</div>
    </div>
    <p class="tagline">Onsite Training – We can come to you</p>
    <p class="benefits">Time efficient<span class="sep">|</span>Cost effective<span class="sep">|</span>Minimise downtime for your team</p>
    <p class="services">First Aid Training | WHS Training</p>

    <div class="band band--bottom" role="img" aria-label="Decorative red and grey band"></div>
  </section>

  <section class="card card--back">
    <div class="contact">
      <h1 class="contact__name">Daniel Hartley</h1>
      <ul class="contact__list">
        <li class="contact__item">
          <svg class="contact__icon" viewBox="0 0 24 24" aria-hidden="true"><path d="M6.6 10.8a15.1 15.1 0 0 0 6.6 6.6l2.2-2.2a1 1 0 0 1 1-.25c1.1.37 2.3.57 3.6.57a1 1 0 0 1 1 1V20a1 1 0 0 1-1 1A17 17 0 0 1 3 4a1 1 0 0 1 1-1h3.5a1 1 0 0 1 1 1c0 1.25.2 2.45.57 3.57a1 1 0 0 1-.25 1z"/></svg>
          <span>0412 386 904</span>
        </li>
        <li class="contact__item">
          <svg class="contact__icon" viewBox="0 0 24 24" aria-hidden="true"><path d="M2 5h20v2.2l-10 6.3L2 7.2z"/><path d="M2 9.6l10 6.3 10-6.3V19H2z"/></svg>
          <span>help@brindlewoodfa.com.au</span>
        </li>
        <li class="contact__item">
          <svg class="contact__icon" viewBox="0 0 24 24" aria-hidden="true"><path d="M12 2a10 10 0 1 0 0 20 10 10 0 0 0 0-20zm6.9 6h-3a15.6 15.6 0 0 0-1.4-3.6A8 8 0 0 1 18.9 8zM12 4c.8 1.2 1.5 2.5 1.9 4h-3.8c.4-1.5 1.1-2.8 1.9-4zM4.3 14a8.2 8.2 0 0 1 0-4h3.4a16 16 0 0 0 0 4zm.8 2h3a15.6 15.6 0 0 0 1.4 3.6A8 8 0 0 1 5.1 16zm3-8h-3a8 8 0 0 1 4.4-3.6A15.6 15.6 0 0 0 8.1 8zM12 20c-.8-1.2-1.5-2.5-1.900-4h3.8c-.4 1.5-1.1 2.8-1.9 4zm2.3-6H9.7a14.6 14.6 0 0 1 0-4h4.6a14.6 14.6 0 0 1 0 4zm.2 5.6a15.6 15.6 0 0 0 1.4-3.6h3a8 8 0 0 1-4.4 3.6zm1.8-5.6a16 16 0 0 0 0-4h3.4a8.2 8.2 0 0 1 0 4z"/></svg>
          <span>brindlewoodfa.com.au</span>
        </li>
      </ul>
    </div>

    <span class="divider"></span>

    <div class="back-brand">
      <span class="back-brand__dot"></span>
      <div class="back-brand__name">BRINDLEWOOD<br>FIRST AID</div>
    </div>

    <div class="band band--bottom" role="img" aria-label="Decorative red and grey band"></div>
  </section>
</body>
</html>
```